Business Consulting Business Card

professional business card with basic information (1) First and Last name (2) email address, (3) phone number, (4) website.

```html
<!DOCTYPE html>
<html lang="en">
<head>
<meta charset="utf-8">
<title>Tidewell Business Card</title>
<link href="https://fonts.googleapis.com/css2?family=Montserrat:wght@400;500;700&display=swap" rel="stylesheet">
<style>
  :root {
    --backdrop: #222426;
    --navy: #0a2d42;
    --teal: #4fc0be;
    --sky: #43a6c9;
    --white: #ffffff;
    --ink: #0b2a3c;
  }
  * { margin: 0; padding: 0; box-sizing: border-box; }
  html, body { width: 1200px; height: 900px; overflow: hidden; }
  body {
    background: var(--backdrop);
    font-family: "Montserrat", Arial, sans-serif;
    position: relative;
  }
  .card {
    position: absolute;
    left: 250px;
    width: 700px;
    height: 400px;
    overflow: hidden;
    box-shadow: 0 14px 30px rgba(0,0,0,0.55);
  }
  .card--front { top: 36px; background: var(--navy); }
  .card--back { top: 464px; background: var(--white); }

  .brand { display: flex; align-items: center; gap: 18px; }
  .brand__dot { width: 46px; height: 46px; border-radius: 50%; background: var(--teal); flex: none; }
  .brand__name { font-weight: 500; letter-spacing: 0.28em; font-size: 30px; }

  .card--front .brand {
    position: absolute; left: 0; right: 0; top: 0; bottom: 0;
    flex-direction: column; justify-content: center; gap: 22px;
  }
  .card--front .brand__dot { width: 64px; height: 64px; }
  .card--front .brand__name { color: var(--white); font-size: 32px; padding-left: 0.28em; }

  .card--back .brand { position: absolute; left: 34px; top: 40px; }
  .card--back .brand__name { color: var(--ink); }

  .person { position: absolute; right: 40px; top: 138px; text-align: right; }
  .person__name { color: var(--sky); font-weight: 700; font-size: 25px; letter-spacing: 0.03em; }
  .person__role { color: var(--ink); font-size: 18px; margin-top: 2px; }

  .wave { position: absolute; left: 0; top: 0; width: 700px; height: 400px; }

  .contacts {
    position: absolute; right: 40px; bottom: 32px;
    list-style: none; color: var(--white); font-size: 20px; line-height: 1.5;
  }
  .contacts li { display: flex; align-items: center; justify-content: flex-end; gap: 14px; }
  .contacts svg { width: 22px; height: 22px; flex: none; }
  .contacts .accent { color: var(--sky); font-weight: 700; }
</style>
</head>
<body>
  <section class="card card--front">
    <div class="brand">
      <span class="brand__dot"></span>
      <span class="brand__name">TIDEWELL</span>
    </div>
  </section>

  <section class="card card--back">
    <svg class="wave" viewBox="0 0 700 400" aria-hidden="true">
      <defs>
        <linearGradient id="band" x1="0" x2="1" y1="0" y2="0">
          <stop offset="0" stop-color="#45a8c8"/>
          <stop offset="1" stop-color="#52c3bd"/>
        </linearGradient>
      </defs>
      <path d="M0 300 C 200 292 380 196 560 188 C 630 186 675 206 700 222 L700 400 L0 400 Z" fill="url(#band)"/>
      <path d="M0 322 C 160 316 300 262 440 232" fill="none" stroke="#ffffff" stroke-width="7"/>
      <path d="M0 400 L0 345 C 200 332 380 226 560 214 C 622 211 670 228 700 246 L700 400 Z" fill="var(--navy)"/>
    </svg>

    <div class="brand">
      <span class="brand__dot"></span>
      <span class="brand__name">TIDEWELL</span>
    </div>

    <div class="person">
      <div class="person__name">MARCUS ELLERY</div>
      <div class="person__role">Managing Broker</div>
    </div>

    <ul class="contacts">
      <li>(305) 555-0148
        <svg viewBox="0 0 24 24" fill="none" stroke="#43a6c9" stroke-width="1.8"><circle cx="12" cy="12" r="10"/><path d="M8.5 7.5l2 2-1 1.5c.8 1.6 1.9 2.7 3.5 3.5l1.5-1 2 2-1.2 1.5c-3.6-.3-7.5-4.2-7.8-7.8z"/></svg>
      </li>
      <li>info@tidewell.com
        <svg viewBox="0 0 24 24" fill="none" stroke="#43a6c9" stroke-width="1.8"><rect x="3" y="6" width="18" height="12" rx="1"/><path d="M3 7l9 6 9-6"/></svg>
      </li>
      <li><span>www.<span class="accent">tidewell</span>.com</span>
        <svg viewBox="0 0 24 24" fill="none" stroke="#43a6c9" stroke-width="1.8"><circle cx="12" cy="12" r="9"/><path d="M3 12h18M12 3c3 3 3 15 0 18M12 3c-3 3-3 15 0 18"/></svg>
      </li>
    </ul>
  </section>
</body>
</html>
```